If everything digital fails, here's what to do

Hi, I would like a poster / infographic of a list of practical actions people could take in case the internet stops working. I've put together a list of 8 areas, with the situation for each, and the mitigation actions folks can take - I need it presented in a clear and aesthetically pleasing way. I will send you the file with the full text so you can include it all

General population, but likely people who are safety conscious and want to protect themselves and learn more about what to do to be tech literate and prepared

Tech / Cyber / Public safety / Civic tech

Sans Serif

• It's a lot of text, so I think the important thing is to have it all in one poster, or in a series of similar pages
• I would like it to be a bit brooding, but also elicit competence and that some experts have thought about this and it will all be okay
• I don't want it to look cartoonish, or cheap - less is more is sort of what I'm looking for

```html
<!DOCTYPE html>
<html lang="en">
<head>
<meta charset="utf-8">
<title>If Everything Digital Fails – Here's What To Do</title>
<link href="https://fonts.googleapis.com/css2?family=Montserrat:wght@400;500;700;800;900&display=swap" rel="stylesheet">
<style>
  :root {
    --brand-blue: #1068b2;
    --ink: #1b1b1b;
    --subhead: #333333;
    --body: #2a2a2a;
    --paper: #ffffff;
  }
  * { box-sizing: border-box; margin: 0; padding: 0; }
  html, body { width: 1200px; height: 3750px; overflow: hidden; background: var(--paper); }
  body { font-family: "Montserrat", Arial, sans-serif; color: var(--body); }
  .poster { position: relative; width: 1200px; height: 3750px; overflow: hidden; background: var(--paper); }

  .top-band { position: absolute; left: 0; top: 0; width: 1200px; height: 113px; background: var(--brand-blue); }

  .title {
    position: absolute; left: 0; top: 172px; width: 1200px; text-align: center;
    font-weight: 900; color: var(--brand-blue); font-size: 110px; line-height: 98px; letter-spacing: 1px;
  }
  .title-pill {
    position: absolute; left: 245px; top: 387px; width: 710px; height: 83px;
    border-radius: 42px; background: var(--brand-blue); color: #fff;
    font-weight: 500; font-size: 54px; line-height: 83px; text-align: center; letter-spacing: 1px;
  }

  .divider { position: absolute; left: 620px; top: 552px; width: 5px; height: 2786px; background: var(--brand-blue); }

  .section { position: absolute; }
  .section-head { display: flex; align-items: baseline; font-weight: 800; color: var(--ink); font-size: 48px; line-height: 48px; }
  .section-num { flex: none; }
  .section-title { line-height: 48px; }
  .section-body { padding-left: var(--indent); }
  .situation { font-weight: 500; color: var(--subhead); font-size: 40px; line-height: 40px; margin: 6px 0 22px; }
  .action { font-size: 16.5px; line-height: 21px; margin-bottom: 21px; }
  .compact .action { font-size: 16px; line-height: 15.5px; margin-bottom: 16px; }

  .thank-you {
    position: absolute; left: 680px; top: 2628px; font-weight: 900; color: var(--brand-blue);
    font-size: 114px; line-height: 108px; letter-spacing: 1px;
  }
  .corner-swoosh { position: absolute; left: 0; top: 0; }
</style>
</head>
<body>
<main class="poster">
  <div class="top-band"></div>

  <svg class="corner-swoosh" width="1200" height="3750" viewBox="0 0 1200 3750" aria-hidden="true">
    <path d="M1200 2610 C1170 3220 820 3640 0 3750 L1200 3750 Z" fill="var(--brand-blue)"/>
  </svg>

  <h1 class="title">IF EVERYTHING<br>DIGITAL FAILS</h1>
  <div class="title-pill">HERE’S WHAT TO DO</div>

  <div class="divider"></div>

  <!-- Left column -->
  <section class="section compact" style="left:33px; top:548px; width:570px; --indent:45px;">
    <h2 class="section-head"><span class="section-num">1.&nbsp;</span><span class="section-title">COMMUNICATIONS</span></h2>
    <div class="section-body">
      <p class="situation">Cell phones / land-line phone services have stopped working</p>
      <p class="action">1) Buy a two-way hand-held walkie talkie and share the other with close friends.</p>
      <p class="action">Refresh when? Check to ensure your walkie talkie has working batteries every 12 months (and that you know / remember how the walkie talkie itself works)</p>
      <p class="action">2) Share a ‘third space’ safe spot with close contacts in town where you know you could meet in emergency situations if your home was not safe to remain in. Do the same with neighbours and folks who live in your neighbourhood - have a central gathering spot in your hood that you share with others so you can have a convening spot close by.</p>
      <p class="action">Refresh when? Have a quick reminder conversation about this with your close contacts every 12 months to ensure everyone knows that’s the plan</p>
      <p class="action">3) Have a printed list of your close contacts’ home addresses handy, if you don’t know how to get to their places by heart.</p>
      <p class="action">Refresh when? Print a new such document every 12 months to ensure it stays up to date</p>
      <p class="action">4) Have a list of close contacts that might still have a working landline (ie. rotary, not voip-based), or who have a satellite phone</p>
      <p class="action">Refresh when? Remind yourself of this list and refresh it every 12 months or so</p>
      <p class="action">5) Make a list of the people in your life that you care about that may also be affected, and make sure you include individuals in your community that may be vulnerable in such a disruption (they may be older, may live alone, might need access to supply of medication).</p>
      <p class="action">Refresh when? Remind yourself of this list and refresh it every 12 months or so</p>
    </div>
  </section>

  <section class="section" style="left:33px; top:1416px; width:570px; --indent:62px;">
    <h2 class="section-head"><span class="section-num">2.&nbsp;</span><span class="section-title">BANKING</span></h2>
    <div class="section-body">
      <p class="situation">Debit and credit cards have stopped working (in stores; ATMs)</p>
      <p class="action" style="width:270px;">Have $500 in cash available in $20 bills.<br>Refresh when? N/A once done</p>
    </div>
  </section>

  <section class="section" style="left:33px; top:1704px; width:570px; --indent:64px;">
    <h2 class="section-head"><span class="section-num">3.&nbsp;</span><span class="section-title">BANKING</span></h2>
    <div class="section-body">
      <p class="situation">Debit and credit cards have stopped working; your bank can’t access its own information (online)</p>
      <p class="action" style="width:400px;">Print paper records of your banking statements that prove what you have in your bank accounts and store it in a safe place in your living space. Ensure it has dates showing and full amounts, as well as your identifiers (name and account numbers) as well as the institution itself (printed screenshots should work fine if your money is in a few accounts requiring many statements). Note the same goes for your liabilities (i.e. be able to prove how much you had left on your mortgage or other bigger loans, if you have such debt).<br>Refresh when? Update this document every 6-12 months</p>
    </div>
  </section>

  <section class="section" style="left:33px; top:2329px; width:570px; --indent:62px;">
    <h2 class="section-head"><span class="section-num">4.&nbsp;</span><span class="section-title">TRANSPORTATION</span></h2>
    <div class="section-body">
      <p class="situation" style="margin-bottom:12px;">Gas stations have stopped working</p>
      <p class="action">(If you own a car) Have a standard 40L gas canister filled with gas and available close by in case needed.</p>
      <p class="action">(Refresh when? Use up the gas within 4 months or so, and refill the canister then (i.e. 3 times a year) so that it remains usable</p>
      <p class="action">(Safety note: (If relevant) ensure the can is not in a place where kids can get to it, since it’s not safe for kids to be around gas</p>
    </div>
  </section>

  <section class="section" style="left:33px; top:2751px; width:570px; --indent:58px;">
    <h2 class="section-head"><span class="section-num">5.&nbsp;</span><span class="section-title">INFORMATION<br>MANAGEMENT</span></h2>
    <div class="section-body">
      <p class="situation" style="margin-top:12px;">Cloud storage services have stopped working</p>
      <p class="action" style="width:400px;">Do a backup of the important documents that are stored only in your cloud storage (e.g. that important email in your Postbox Mail; that tax document only issued digitally, etc.)</p>
      <p class="action" style="width:400px;">Refresh when? Do a backup and update every 6 months</p>
      <p class="action" style="width:400px;">Note: Since this is a time-consuming exercise but not necessarily the same exercise as #7 below, you could alternate the months when you do one versus the other. For example, you could do this with annual equinoxes: March 21 and Sept 21 (pro tip: star email messages that are important as they arrive, so that you know what needs to be backed up every six months; that way, you don’t have to go searching through your whole inbox)</p>
    </div>
  </section>

  <!-- Right column -->
  <section class="section" style="left:670px; top:553px; width:500px; --indent:60px;">
    <h2 class="section-head"><span class="section-num">6.&nbsp;</span><span class="section-title">INFORMATION<br>MANAGEMENT</span></h2>
    <div class="section-body">
      <p class="situation" style="margin-top:10px;">Password manager services (cloud) have stopped working</p>
      <p class="action">Preamble: Many individuals don’t remember their passwords anymore, having password managers generate complicated strings of characters as their passwords for their many digital accounts in their lives.</p>
      <p class="action">Print a full list of your accounts and their passwords and keep that document safely in your living space.</p>
      <p class="action">Refresh when? Print a new such document every 6 months to ensure the list remains up to date</p>
    </div>
  </section>

  <section class="section" style="left:670px; top:1166px; width:500px; --indent:56px;">
    <h2 class="section-head"><span class="section-num">7.&nbsp;</span><span class="section-title">TECHNOLOGY</span></h2>
    <div class="section-body">
      <p class="situation">Computers (laptops, tablets, smart phones) have stopped working</p>
      <p class="action">1) Save all important digital materials (e.g. photos) that don’t also exist on paper on a portable hard drive. Remember to do this for all digital materials that have been saved to your cloud that you might have forgotten about (archived, etc.).</p>
      <p class="action">Refresh when? Do a backup and update every 6 months</p>
      <p class="action">Note: Since this is time-consuming, put a note in your calendar at the beginning of the year, choosing the time and date when you will do this (as noted in #5 above, you could do this in line with the solstice each year: June 20 and December 20)</p>
      <p class="action">2) Get a hand cranked radio to ensure you have access to important news and information about what’s happening in your community (locally, as well as nationally/ internationally).</p>
      <p class="action">Refresh when? Make sure the hand cranked radio has fresh batteries (change them every 12 months or so</p>
      <p class="action">3) Download a copy of your city’s maps (e.g. Wayfind Maps) on your phone for local access, and make sure you have a physical map in case you need to get somewhere new in your city in a rush, and you don’t know how to get there.</p>
      <p class="action">Refresh when: N/A once done</p>
    </div>
  </section>

  <section class="section" style="left:670px; top:2132px; width:500px; --indent:58px;">
    <h2 class="section-head"><span class="section-num">8.&nbsp;</span><span class="section-title">TECHNOLOGY</span></h2>
    <div class="section-body">
      <p class="situation">Smart home devices have stopped working</p>
      <p class="action" style="width:275px;">If you have a smart home device that needs to be connected to the internet to work and that doesn’t have a manual override (e.g. a smart lock for your living space’s main door, or for the garage) ensure you have a backup system in place that would not leave you stranded when the internet goes down.</p>
      <p class="action">Refresh when: N/A once done</p>
    </div>
  </section>

  <p class="thank-you">THANK<br>YOU!</p>
</main>
</body>
</html>
```